Social Media Overlay for Ormond Real Estate

We need an social media overlay that can be added to a photo of a house that includes our current logo and a call to action of "Just Listed". This needs to be something that we can use for every new house that we list. Attached is our current logo in both company colors, purple and white. An example of a overlay from Plazeo that we like.

Target Market(s)

Social Media Real Estate Community - Real Estate Agents, Brokers, Buyers & Sellers

Industry/Entity Type

Real Estate

Font styles to use
Sans Serif

Colors
6c459b

Requirements
Must have
• the company colors, purple and white and the company logo
Nice to have
• call to action "Just Listed"
• some layered, texture, or 3-D effect
Should not have
• Should be clean and simple; nothing too busy

```html
<!DOCTYPE html>
<html lang="en">
<head>
<meta charset="utf-8">
<title>Ormond Real Estate — Just Listed Overlays</title>
<link href="https://fonts.googleapis.com/css2?family=Open+Sans:wght@400;600;700&display=swap" rel="stylesheet">
<style>
  :root {
    --brand-purple: #5c2d87;
    --brand-purple-soft: #7a4fa6;
    --brand-white: #ffffff;
    --card-light: #efeff0;
    --board: #dcdcdd;
    --pin-red: #d3212c;
    --photo-sky: #5aa6de;
    --photo-trees: #3f6a33;
    --photo-house: #d8d2c2;
    --photo-ground: #e4ddd0;
  }
  * { box-sizing: border-box; margin: 0; padding: 0; }
  html, body {
    width: 1200px; height: 923px; overflow: hidden;
    background: var(--board);
    font-family: "Open Sans", Arial, sans-serif;
  }
  .board { position: relative; width: 1200px; height: 923px; }

  .overlay-card {
    position: absolute; width: 542px; height: 323px; overflow: visible;
  }
  .overlay-card--light { background: linear-gradient(180deg, #f6f6f7, var(--card-light)); }
  .overlay-card--purple { background: var(--brand-purple); }
  .pos-tl { left: 40px;  top: 71px; }
  .pos-tr { left: 618px; top: 71px; }
  .pos-bl { left: 40px;  top: 499px; }
  .pos-br { left: 618px; top: 499px; }

  .house-photo {
    position: absolute; left: 25px; top: 15px; width: 491px; height: 260px;
    border: 3px solid var(--brand-white);
    background: linear-gradient(180deg,
      var(--photo-sky) 0%, #8cc2e6 14%,
      var(--photo-trees) 24%, #5b8046 42%,
      var(--photo-house) 52%, #cfc6b3 78%,
      var(--photo-ground) 88%, #d9d4c6 100%);
    box-shadow: 0 10px 10px -6px rgba(0,0,0,0.45);
  }

  .brand-logo {
    position: absolute; left: 0; right: 0; top: 280px;
    text-align: center; font-weight: 600; line-height: 1;
  }
  .overlay-card--light .brand-logo { color: var(--brand-purple); }
  .overlay-card--purple .brand-logo { color: var(--brand-white); }
  .brand-logo__name { display: block; font-size: 25px; letter-spacing: -0.5px; }
  .brand-logo__tag  { display: block; font-size: 11.5px; margin-top: 3px; }

  .note-tag {
    position: absolute; left: 17px; top: 22px; width: 88px; height: 70px;
    transform: rotate(-8deg);
    display: flex; align-items: center; justify-content: center;
    text-align: center; font-weight: 600; font-size: 18.5px; line-height: 1.05;
    letter-spacing: 0.5px;
    box-shadow: 3px 4px 6px rgba(0,0,0,0.35);
  }
  .note-tag--purple { background: var(--brand-purple-soft); color: var(--brand-white); }
  .note-tag--white  { background: var(--brand-white); color: var(--brand-purple-soft); }
  .note-tag__pin {
    position: absolute; top: -6px; left: 38px; width: 10px; height: 10px;
    border-radius: 50%; background: var(--pin-red);
    box-shadow: 1px 2px 2px rgba(0,0,0,0.4);
  }

  .stamp { position: absolute; left: 414px; top: 198px; width: 124px; height: 100px; }
  .stamp text {
    font-family: "Open Sans", Arial, sans-serif; font-weight: 700; font-size: 26px;
    fill: var(--brand-purple); stroke: var(--brand-white); stroke-width: 2.5px;
    paint-order: stroke;
  }
</style>
</head>
<body>
<main class="board">

  <section class="overlay-card overlay-card--light pos-tl">
    <div class="house-photo" role="img" aria-label="Photo of the listed house"></div>
    <div class="note-tag note-tag--purple"><span class="note-tag__pin"></span>JUST<br>LISTED</div>
    <div class="brand-logo"><span class="brand-logo__name">Ormond</span><span class="brand-logo__tag">Real Estate</span></div>
  </section>

  <section class="overlay-card overlay-card--purple pos-tr">
    <div class="house-photo" role="img" aria-label="Photo of the listed house"></div>
    <div class="note-tag note-tag--white"><span class="note-tag__pin"></span>JUST<br>LISTED</div>
    <div class="brand-logo"><span class="brand-logo__name">Ormond</span><span class="brand-logo__tag">Real Estate</span></div>
  </section>

  <section class="overlay-card overlay-card--light pos-bl">
    <div class="house-photo" role="img" aria-label="Photo of the listed house"></div>
    <svg class="stamp" viewBox="0 0 124 100" aria-label="Just Listed">
      <g transform="rotate(-20 62 50)">
        <circle cx="62" cy="50" r="42" fill="none" stroke="#ffffff" stroke-width="5"/>
        <circle cx="62" cy="50" r="42" fill="none" stroke="var(--brand-purple)" stroke-width="2.5"/>
        <line x1="2" y1="36" x2="118" y2="36" stroke="var(--brand-purple)" stroke-width="2.5"/>
        <line x1="8" y1="84" x2="122" y2="84" stroke="var(--brand-purple)" stroke-width="2.5"/>
        <text x="62" y="58" text-anchor="middle">JUST</text>
        <text x="64" y="82" text-anchor="middle">LISTED</text>
      </g>
    </svg>
    <div class="brand-logo"><span class="brand-logo__name">Ormond</span><span class="brand-logo__tag">Real Estate</span></div>
  </section>

  <section class="overlay-card overlay-card--purple pos-br">
    <div class="house-photo" role="img" aria-label="Photo of the listed house"></div>
    <svg class="stamp" viewBox="0 0 124 100" aria-label="Just Listed">
      <g transform="rotate(-20 62 50)">
        <circle cx="62" cy="50" r="42" fill="none" stroke="#ffffff" stroke-width="5"/>
        <circle cx="62" cy="50" r="42" fill="none" stroke="var(--brand-purple)" stroke-width="2.5"/>
        <line x1="2" y1="36" x2="118" y2="36" stroke="var(--brand-purple)" stroke-width="2.5"/>
        <line x1="8" y1="84" x2="122" y2="84" stroke="var(--brand-purple)" stroke-width="2.5"/>
        <text x="62" y="58" text-anchor="middle">JUST</text>
        <text x="64" y="82" text-anchor="middle">LISTED</text>
      </g>
    </svg>
    <div class="brand-logo"><span class="brand-logo__name">Ormond</span><span class="brand-logo__tag">Real Estate</span></div>
  </section>

</main>
</body>
</html>
```